I challenge you to create Denmark's coolest roofing company website

We need to have a website created for our roofing company.

I have some pages that can be used as a starting point because there are some things we would like to have, one important thing is a roof calculator, in addition to that information about the company, pictures of tasks we have completed, links to Friendlio and Pictavoro pages.

reviews from rated, etc. should also be visible on the page.

we have lots of pictures, videos, logos,

we need to have a nice home page that is just a little cooler than the competitors.
we need to steal their customer. the page should be easy and clear but with a nice design.
an important thing is the calculator.
come up with some suggestions we are quite open as long as it is a nice design
Updates

I have made an update in the PDF file with some thoughts and wishes. The file has been uploaded.

Target Market(s)

20-60

Industry/Entity Type

carpenter - roofer

Coding

Coded - Design and coding required

Number of Pages Required

4 page

Font styles to use
Sans Serif

Colors
EB3D1F
EC4F4E
F09395
F8D3D4
FCEDEE

Requirements
Must have
• Roof calculator, nice design, easy to get around
Nice to have
• the competitors : https://mollerbyghuset.dk https://hvid-tegl.dk https://strandbyghuset.dk

```html
<!DOCTYPE html>
<html lang="en">
<head>
<meta charset="utf-8">
<title>Tagværket – Expert Roofing Solutions</title>
<link href="https://fonts.googleapis.com/css2?family=Poppins:wght@400;500;600;700&display=swap" rel="stylesheet">
<style>
:root{
  --red:#c41e35;
  --red-dark:#a3162a;
  --black:#111111;
  --card:#2b2b2b;
  --white:#ffffff;
  --text:#222222;
  --muted:#666666;
  --line:#dddddd;
  --grey-bg:#f4f4f4;
}
*{box-sizing:border-box;margin:0;padding:0}
html,body{width:1200px;height:4572px;overflow:hidden}
body{font-family:'Poppins',sans-serif;color:var(--text);background:var(--white);position:relative}
.btn{display:inline-block;background:var(--red);color:var(--white);font-size:13px;font-weight:600;text-transform:uppercase;letter-spacing:.5px;padding:12px 30px;border-radius:30px}
.btn-light{background:var(--white);color:var(--red)}
.accent{color:var(--red)}
.section-title{text-align:center;font-size:40px;font-weight:600}

/* hero */
.hero{position:absolute;top:0;left:0;width:1200px;height:632px;overflow:hidden}
.hero-photo{position:absolute;inset:0;background:linear-gradient(160deg,#6d7378 0%,#3d4246 35%,#5b4a40 60%,#b5642c 78%,#40444a 100%)}
.hero-shade{position:absolute;inset:0;background:rgba(0,0,0,.35)}
.nav{position:absolute;top:20px;left:120px;width:960px;height:84px;background:var(--white);border-radius:12px;display:flex;align-items:center;padding:0 28px}
.logo{display:flex;align-items:center;gap:10px;font-size:24px;font-weight:700;color:var(--text)}
.logo-mark{width:18px;height:18px;background:var(--red)}
.nav-links{display:flex;gap:34px;margin-left:auto;margin-right:28px;font-size:15px}
.nav-links .active{color:var(--red);border-bottom:2px solid var(--red);padding-bottom:4px}
.hero-arrow{position:absolute;top:350px;width:14px;height:14px;border-left:3px solid var(--white);border-bottom:3px solid var(--white)}
.hero-arrow.left{left:30px;transform:rotate(45deg)}
.hero-arrow.right{right:30px;transform:rotate(-135deg)}
.hero-content{position:absolute;top:262px;left:0;width:1200px;text-align:center;color:var(--white)}
.hero-kicker{font-size:14px;letter-spacing:1.5px;text-transform:uppercase}
.hero-title{font-size:62px;font-weight:600;line-height:1.18;margin-top:8px}
.hero-title span{font-size:54px}
.hero-sub{font-size:16px;margin:14px 0 20px}

/* dark */
.dark{position:absolute;top:632px;left:0;width:1200px;height:1488px;background:var(--black);color:var(--white)}
.about-card{position:absolute;top:56px;left:60px;width:1080px;height:532px;background:var(--white);border-radius:24px;color:var(--text)}
.about-text{position:absolute;left:100px;top:90px;width:420px}
.about-text h2{font-size:36px;font-weight:600;margin-bottom:20px}
.about-text p{font-size:14.5px;line-height:1.6;color:var(--muted);margin-bottom:30px}
.about-photo{position:absolute;left:540px;top:80px;width:440px;height:384px;border-radius:18px;background:linear-gradient(180deg,#7fb2dd 0%,#a9cbe8 30%,#d9662c 45%,#c55420 62%,#3b4654 70%,#2f3947 100%)}
.play{position:absolute;right:22px;bottom:22px;width:64px;height:64px;border-radius:50%;background:rgba(255,255,255,.85);display:flex;align-items:center;justify-content:center}
.why-title{position:absolute;top:660px;width:1200px;color:var(--white)}
.why-row{position:absolute;top:740px;left:100px;width:1000px;display:flex;justify-content:space-between}
.why-item{width:300px;text-align:center}
.why-icon{width:96px;height:96px;margin:0 auto 26px;border:2px solid var(--white);border-radius:50%;display:flex;align-items:center;justify-content:center}
.why-item h3{font-size:20px;font-weight:600;margin-bottom:8px}
.why-item p{font-size:14px;line-height:1.5;color:#ccc}
.why-arrow{position:absolute;top:44px}
.services-title{position:absolute;top:1010px;width:1200px;color:var(--white)}
.services{position:absolute;top:1096px;left:68px;width:1064px;display:flex;gap:22px}
.service{width:250px;height:320px;background:var(--card);border-radius:14px;text-align:center;padding:56px 26px 0}
.service.featured{background:var(--red)}
.service svg{margin-bottom:22px}
.service h3{font-size:19px;font-weight:600;margin-bottom:10px}
.service p{font-size:12.5px;line-height:1.5;color:#ddd;margin-bottom:22px}
.service .more{font-size:12px;font-weight:600;letter-spacing:.5px}

/* experts */
.experts-title{position:absolute;top:2160px;width:1200px}
.team{position:absolute;top:2260px;left:160px;width:880px;display:flex;gap:16px}
.member{width:208px;height:268px;position:relative}
.member-photo{width:208px;height:240px;background:linear-gradient(180deg,#e7e5e2,#c9c4bd)}
.member-name{position:absolute;left:16px;right:16px;bottom:0;height:62px;background:var(--black);color:var(--white);font-size:14px;display:flex;align-items:center;justify-content:center}
.team-btn{position:absolute;top:2574px;width:1200px;text-align:center}

/* projects */
.projects-title{position:absolute;top:2644px;width:1200px}
.projects{position:absolute;top:2740px;left:160px;width:880px;display:grid;grid-template-columns:428px 428px;gap:24px}
.project{height:302px;border-radius:10px}
.p1{background:linear-gradient(160deg,#e0682c,#c4511f 60%,#8e3a18)}
.p2{background:linear-gradient(180deg,#8fb7dc 0%,#3a3d42 35%,#2d3034 100%)}
.p3{background:linear-gradient(180deg,#9ec3e4 0%,#b6b8b9 40%,#8b7460 100%)}
.p4{background:linear-gradient(180deg,#a9c9e6 0%,#c9c7c3 45%,#6d6e70 100%)}
.projects-btn{position:absolute;top:3410px;width:1200px;text-align:center}

/* feedback */
.feedback-title{position:absolute;top:3490px;width:1200px}
.reviews{position:absolute;top:3588px;left:180px;width:860px;display:flex;gap:60px}
.review{width:400px;position:relative}
.review-head{display:flex;align-items:center;gap:16px;margin-bottom:16px}
.avatar{width:58px;height:58px;background:#c9c2ba}
.review-head b{display:block;font-size:17px;font-weight:600}
.review-head small{font-size:14px;font-weight:600}
.quote{position:absolute;right:0;top:0;font-size:80px;line-height:.8;color:#c7c7c7;font-weight:700}
.review p{font-size:13.5px;line-height:1.55;color:var(--muted);padding-bottom:18px;border-bottom:1px solid var(--line)}
.dots{position:absolute;top:3786px;width:1200px;display:flex;justify-content:center;gap:10px}
.dots i{width:8px;height:8px;border-radius:50%;background:#ccc}
.dots i.on{background:var(--red)}

/* cta */
.cta{position:absolute;top:3860px;left:108px;width:984px;height:340px;background:var(--red);border-radius:30px;color:var(--white);text-align:center;padding-top:60px}
.cta h2{font-size:38px;font-weight:600;line-height:1.25}
.cta p{width:680px;margin:18px auto 24px;font-size:14px;line-height:1.55}

/* footer */
.footer-logo{position:absolute;top:4262px;width:1200px;display:flex;justify-content:center}
.footer-logo .logo{font-size:38px}
.footer-logo .logo-mark{width:26px;height:26px}
.footer-nav{position:absolute;top:4400px;left:270px;width:660px;display:flex;justify-content:space-between;font-size:14px;font-weight:500;padding:0 40px}
.footer-line{position:absolute;left:160px;width:880px;height:1px;background:var(--line)}
.contacts{position:absolute;top:4452px;left:260px;width:680px;display:flex;justify-content:space-between;font-size:14px;color:var(--muted)}
.contacts span{display:flex;align-items:center;gap:10px}
.contacts i{width:30px;height:30px;border-radius:50%;background:var(--red);display:flex;align-items:center;justify-content:center}
.social{position:absolute;top:4528px;width:1200px;display:flex;justify-content:center;gap:20px}
.social i{width:20px;height:20px;border-radius:50%;background:var(--red)}
</style>
</head>
<body>

<header class="hero">
  <div class="hero-photo" role="img" aria-label="Roofer in orange safety gear working on a tiled roof"></div>
  <div class="hero-shade"></div>
  <nav class="nav">
    <div class="logo"><span class="logo-mark"></span>Tagværket</div>
    <div class="nav-links">
      <span class="active">Home</span><span>About Us</span><span>Services</span><span>Testimonial</span><span>Contact Us</span>
    </div>
    <span class="btn">Price Calculator</span>
  </nav>
  <span class="hero-arrow left"></span><span class="hero-arrow right"></span>
  <div class="hero-content">
    <div class="hero-kicker">Welcome to Tagværket</div>
    <h1 class="hero-title">Protect Your Home with<br><span>Expert Roofing Solutions</span></h1>
    <p class="hero-sub">Easy Estimates • Certified Roofers • Trusted Locally</p>
    <span class="btn">Learn More</span>
  </div>
</header>

<section class="dark">
  <div class="about-card">
    <div class="about-text">
      <h2>About <span class="accent">Us</span></h2>
      <p>Lorem Ipsum is simply dummy text of the printing and typesetting industry. Lorem Ipsum has been the industry's standard dummy text ever since the 1500s, when an unknown printer took a galley of type and scrambled it to make a type specimen book. It has survived not only five centuries, but also the leap into electronic typesetting, remaining essentially unchanged.</p>
      <span class="btn">Learn More</span>
    </div>
    <div class="about-photo" role="img" aria-label="House with a new orange tiled roof under blue sky">
      <span class="play"><svg width="22" height="24" viewBox="0 0 22 24"><path d="M2 2 L20 12 L2 22 Z" fill="#c41e35"/></svg></span>
    </div>
  </div>

  <h2 class="section-title why-title">Why Choose <span class="accent">Tagværket</span></h2>
  <div class="why-row">
    <div class="why-item">
      <div class="why-icon"><svg width="44" height="44" viewBox="0 0 44 44" fill="none" stroke="#fff" stroke-width="2.5"><circle cx="22" cy="22" r="18"/><path d="M22 11 V22 L30 27"/></svg></div>
      <h3>Save Time And Money</h3>
      <p>Lorem Ipsum is simply dummy text of the printing and typesetting industry.</p>
    </div>
    <div class="why-item">
      <div class="why-icon"><svg width="44" height="44" viewBox="0 0 44 44" fill="none" stroke="#fff" stroke-width="2.5"><path d="M22 4 L38 10 V22 C38 32 30 38 22 41 C14 38 6 32 6 22 V10 Z"/><path d="M15 22 L20 27 L30 16"/></svg></div>
      <h3>Our Team Keeps It Clean</h3>
      <p>Lorem Ipsum is simply dummy text of the printing and typesetting industry.</p>
    </div>
    <div class="why-item">
      <div class="why-icon"><svg width="44" height="44" viewBox="0 0 44 44" fill="none" stroke="#fff" stroke-width="2.5"><path d="M6 22 L22 8 L38 22"/><path d="M10 22 V38 H34 V22"/><path d="M10 30 H34 M18 22 V38 M26 22 V38"/></svg></div>
      <h3>Technology On Your Side</h3>
      <p>Lorem Ipsum is simply dummy text of the printing and typesetting industry.</p>
    </div>
    <svg class="why-arrow" style="left:318px" width="50" height="10" viewBox="0 0 50 10"><path d="M0 5 H44 M40 1 L46 5 L40 9" stroke="#fff" stroke-width="1.5" fill="none" stroke-dasharray="4 3"/></svg>
    <svg class="why-arrow" style="left:632px" width="50" height="10" viewBox="0 0 50 10"><path d="M0 5 H44 M40 1 L46 5 L40 9" stroke="#fff" stroke-width="1.5" fill="none" stroke-dasharray="4 3"/></svg>
  </div>

  <h2 class="section-title services-title">Our <span class="accent">Services</span></h2>
  <div class="services">
    <div class="service">
      <svg width="60" height="56" viewBox="0 0 60 56" fill="#fff"><path d="M30 4 L56 28 H48 V52 H12 V28 H4 Z"/></svg>
      <h3>New Roof</h3>
      <p>It is a long established fact that a reader will be distracted by its layout.</p>
      <span class="more">LEARN MORE</span>
    </div>
    <div class="service">
      <svg width="60" height="56" viewBox="0 0 60 56" fill="none" stroke="#fff" stroke-width="3"><path d="M4 30 L30 6 L56 30"/><path d="M14 28 L30 14 L46 28 V50 H14 Z"/><path d="M22 40 H38 M22 33 H38"/></svg>
      <h3>Roof Renovation</h3>
      <p>It is a long established fact that a reader will be distracted by its layout.</p>
      <span class="more">LEARN MORE</span>
    </div>
    <div class="service featured">
      <svg width="60" height="56" viewBox="0 0 60 56" fill="none" stroke="#fff" stroke-width="3"><path d="M6 50 H54"/><path d="M12 50 L34 20 L48 50"/><path d="M40 6 L28 18 M34 6 L46 18"/></svg>
      <h3>Acute Injuries</h3>
      <p>It is a long established fact that a reader will be distracted by its layout.</p>
      <span class="more">LEARN MORE</span>
    </div>
    <div class="service">
      <svg width="60" height="56" viewBox="0 0 60 56" fill="#fff"><path d="M4 50 L34 14 L56 50 Z"/><rect x="40" y="6" width="6" height="14"/></svg>
      <h3>Carpenter</h3>
      <p>It is a long established fact that a reader will be distracted by its layout.</p>
      <span class="more">LEARN MORE</span>
    </div>
  </div>
</section>

<h2 class="section-title experts-title">Meet The <span class="accent">Experts</span></h2>
<div class="team">
  <div class="member"><div class="member-photo" role="img" aria-label="Portrait of team member Anders Holm"></div><div class="member-name">Anders Holm</div></div>
  <div class="member"><div class="member-photo" role="img" aria-label="Portrait of team member Lise Brandt"></div><div class="member-name">Lise Brandt</div></div>
  <div class="member"><div class="member-photo" role="img" aria-label="Portrait of team member Sofie Dahl"></div><div class="member-name">Sofie Dahl</div></div>
  <div class="member"><div class="member-photo" role="img" aria-label="Portrait of team member Jonas Krogh"></div><div class="member-name">Jonas Krogh</div></div>
</div>
<div class="team-btn"><span class="btn">View All Team</span></div>

<h2 class="section-title projects-title">Our <span class="accent">Projects</span></h2>
<div class="projects">
  <div class="project p1" role="img" aria-label="Orange clay tile roof with skylight windows"></div>
  <div class="project p2" role="img" aria-label="Dark grey tiled roof on a house"></div>
  <div class="project p3" role="img" aria-label="Roof under construction with battens"></div>
  <div class="project p4" role="img" aria-label="Large grey tile roof on a modern building"></div>
</div>
<div class="projects-btn"><span class="btn">View All Projects</span></div>

<h2 class="section-title feedback-title">Client <span class="accent">Feedback</span></h2>
<div class="reviews">
  <div class="review">
    <div class="review-head"><div class="avatar" role="img" aria-label="Client photo"></div><div><b>Sara L</b><small>Small Business Owner</small></div></div>
    <span class="quote">“</span>
    <p>The roofing team transformed our support. It’s like having an extra team member who works around the clock.</p>
  </div>
  <div class="review">
    <div class="review-head"><div class="avatar" role="img" aria-label="Client photo"></div><div><b>Mikkel R</b><small>Enterprise Manager</small></div></div>
    <span class="quote">“</span>
    <p>The honest assistance option is a game-changer. Our team loves the flexibility of jumping in when needed.</p>
  </div>
</div>
<div class="dots"><i></i><i class="on"></i><i></i></div>

<section class="cta">
  <h2>Safeguard Your Property With<br>Trusted Roofing Experts</h2>
  <p>Lorem Ipsum is simply dummy text of the printing and typesetting industry. Lorem Ipsum has been the industry's standard dummy text ever since the 1500s, when an unknown printer took a galley of type and scrambled it to make a type specimen book.</p>
  <span class="btn btn-light">Price Calculator</span>
</section>

<footer>
  <div class="footer-logo"><div class="logo"><span class="logo-mark"></span>Tagværket</div></div>
  <div class="footer-line" style="top:4386px"></div>
  <nav class="footer-nav"><span>HOME</span><span>ABOUT US</span><span>SERVICES</span><span>TESTIMONIAL</span><span>CONTACT US</span></nav>
  <div class="footer-line" style="top:4436px"></div>
  <div class="contacts">
    <span><i><svg width="14" height="14" viewBox="0 0 14 14"><path d="M3 1 L5 1 L6 4 L4.5 5 C5.5 7 7 8.5 9 9.5 L10 8 L13 9 L13 11 C13 12 12 13 11 13 C5.5 13 1 8.5 1 3 C1 2 2 1 3 1 Z" fill="#fff"/></svg></i>+45 20 40 60 80</span>
    <span><i><svg width="14" height="12" viewBox="0 0 14 12"><rect x="1" y="1" width="12" height="10" fill="none" stroke="#fff" stroke-width="1.5"/><path d="M1 1 L7 6 L13 1" fill="none" stroke="#fff" stroke-width="1.5"/></svg></i>kontakt@tagvaerket.dk</span>
    <span><i><svg width="12" height="15" viewBox="0 0 12 15"><path d="M6 14 C6 14 1 8.5 1 5.5 A5 5 0 0 1 11 5.5 C11 8.5 6 14 6 14 Z" fill="#fff"/><circle cx="6" cy="5.5" r="1.8" fill="#c41e35"/></svg></i>122, Lorem Ipsum street</span>
  </div>
  <div class="social"><i></i><i></i><i></i><i></i></div>
</footer>

</body>
</html>
```